Sign Shop website

We need a web design for a sign company called Quanta Signs that builds signs for shops such as A Frames, Banners, Tennet Boards, Shop front windows etc...

The existing site is avaliable at www.quantasigns-demo.com.au

We will need to have a fresh makeover. The new site must have the following:

Photo Galleries (broken down into sections)
Store Locations (currently there are 4 stores)
Online quote form
List of services
About Us Page

We just need to front page designed in photoshop (the inner page is not necessary) We have a team that can code the site up.

The website should have the exact logo. Any person who alters the logo, design will be elimated.

No Twitter, RSS, LinkedIn icons

The main colours are yellow, black, blue, red

Target Market(s)

Any business

Industry/Entity Type

It Company

Requirements
Must have
• jQuery slider banner
Should not have
• Alter the logo in any way

```html
<!DOCTYPE html>
<html lang="en">
<head>
<meta charset="utf-8">
<title>Quanta Signs — Home</title>
<link rel="stylesheet" href="https://fonts.googleapis.com/css2?family=Open+Sans:wght@400;600;700&family=Lato:ital,wght@0,400;0,700;1,400&family=Yanone+Kaffeesatz:wght@400;500&family=Kalam&display=swap">
<style>
:root{
  --yellow:#f0b12e;
  --black:#1c1c1c;
  --blue:#2f5593;
  --blue-dark:#21447f;
  --heading:#2b4c85;
  --text:#4a4a4a;
  --muted:#6b6b6b;
  --orange:#f47a12;
  --orange-light:#ff9a2e;
  --rule:#dcdcdc;
  --page:#f4f4f4;
  --footer:#3a3a3a;
  --quote-bg:#f3eeee;
}
*{box-sizing:border-box;margin:0;padding:0}
html,body{width:953px;height:1200px;overflow:hidden}
body{position:relative;background:var(--page);font-family:"Lato",sans-serif;color:var(--text)}
.abs{position:absolute}

/* header */
.site-header{position:absolute;left:0;top:0;width:953px;height:80px;background:var(--yellow);border-bottom:3px solid var(--black)}
.brand{position:absolute;left:127px;top:24px;display:flex;align-items:center;gap:10px}
.brand-mark{width:28px;height:28px;background:var(--black)}
.brand-name{font-family:"Open Sans",sans-serif;font-weight:700;font-size:30px;color:var(--black);letter-spacing:-.5px}
.store-locations{position:absolute;left:678px;top:5px;font-family:"Open Sans",sans-serif;font-weight:700;font-size:9.5px;line-height:11px;color:var(--black);padding-left:20px}
.store-locations svg{position:absolute;left:0;top:1px}
.main-nav{position:absolute;left:431px;top:52px;width:396px;height:28px;background:var(--black);display:flex;font-family:"Open Sans",sans-serif;font-size:11.5px;color:#fff}
.main-nav a{flex:1;display:flex;align-items:center;justify-content:center;color:#fff;text-decoration:none;border-left:1px solid #3a3a3a;position:relative}
.main-nav a:first-child{border-left:none}
.main-nav a.active::after{content:"";position:absolute;left:50%;bottom:-6px;margin-left:-6px;border:6px solid transparent;border-bottom:none;border-top-color:var(--black)}

/* hero slider */
.hero{position:absolute;left:0;top:83px;width:953px;height:328px;background:radial-gradient(ellipse at 55% 45%,#3f68a8 0%,var(--blue) 45%,var(--blue-dark) 100%);overflow:hidden}
.hero-title{position:absolute;left:138px;top:76px;font-family:"Open Sans",sans-serif;font-weight:700;font-size:32px;color:#fff;text-shadow:0 2px 3px rgba(0,0,0,.35)}
.hero-text{position:absolute;left:136px;top:126px;width:310px;font-size:12px;line-height:17.8px;color:#fff}
.slider-dots{position:absolute;left:136px;top:279px;display:flex;gap:3px}
.slider-dots span{width:8px;height:8px;border-radius:50%;background:#1b3764;box-shadow:inset 0 1px 1px rgba(0,0,0,.5)}
.slider-dots span.on{background:#4a6ea8}
.hero-visual{position:absolute;left:556px;top:24px;width:214px;height:270px;background:linear-gradient(180deg,#2a2a2a,#0d0d0d);border-radius:2px}

/* content */
.section-title{position:absolute;font-size:16px;font-weight:700;color:var(--heading);display:flex;align-items:center}
.section-rule{position:absolute;height:1px;background:var(--rule);border-bottom:1px solid #fff}
.welcome-text{position:absolute;left:125px;top:490px;width:522px;font-size:10.6px;line-height:18px;color:var(--text)}
.btn-more{position:absolute;left:125px;top:650px;width:60px;height:19px;border-radius:3px;background:linear-gradient(#4d72b0,#27477f);border:1px solid #1d3766;color:#fff;font-size:11px;font-weight:700;display:flex;align-items:center;justify-content:center}
.owner-badge{position:absolute;left:712px;top:510px}

/* quote form */
.quote-panel{position:absolute;left:354px;top:376px;width:264px;height:465px;background:linear-gradient(#fdfdfd,#eef3f8);border:1px solid #d9dee4;border-radius:3px;box-shadow:0 2px 10px rgba(0,0,0,.25);z-index:5}
.quote-badge{position:absolute;left:34px;top:7px;width:191px;height:48px;border-radius:3px;background:linear-gradient(var(--orange-light),var(--orange));box-shadow:0 2px 3px rgba(0,0,0,.3);text-align:center;color:#fff}
.quote-badge strong{display:block;font-family:"Yanone Kaffeesatz",sans-serif;font-weight:500;font-size:24px;line-height:26px;margin-top:3px}
.quote-badge em{display:block;font-family:"Kalam",cursive;font-style:normal;font-size:10.5px;line-height:13px}
.field-label{position:absolute;left:11px;font-size:10px;color:var(--muted);font-family:"Open Sans",sans-serif}
.field{position:absolute;left:74px;width:176px;height:24px;background:#fff;border:1px solid #b9cfe3;border-radius:2px}
.btn-send{position:absolute;left:176px;top:429px;width:74px;height:25px;border-radius:3px;background:linear-gradient(var(--orange-light),var(--orange));color:#fff;font-family:"Yanone Kaffeesatz",sans-serif;font-size:18px;display:flex;align-items:center;justify-content:center}

/* recent work */
.work-arrow{position:absolute;width:22px;height:21px;display:flex;align-items:center;justify-content:center}
.work-arrow.prev{left:134px;top:791px;background:#cfcfcf}
.work-arrow.next{left:812px;top:791px;background:var(--blue)}
.work-thumb{position:absolute;top:750px;width:134px;height:102px;background:linear-gradient(180deg,#7a3550 0%,#c9b5b8 35%,#3a3a3a 100%)}
.work-thumb.highlight{background:var(--yellow)}

/* why choose / testimonials */
.reasons{position:absolute;left:125px;top:953px;list-style:none}
.reasons li{display:flex;align-items:center;height:25.5px;font-size:10px;color:var(--text)}
.reasons svg{margin-right:5px;flex:none}
.testimonial{position:absolute;left:477px;top:953px;width:336px;height:110px;background:var(--quote-bg);padding:18px 20px;font-style:italic;font-size:9.3px;line-height:14.7px;color:var(--muted)}
.testimonial::after{content:"";position:absolute;left:28px;bottom:-12px;border-left:0 solid transparent;border-right:14px solid transparent;border-top:12px solid var(--quote-bg)}
.author{position:absolute;left:479px;top:1080px;display:flex;align-items:center;gap:14px;font-size:9.5px;color:var(--text)}
.author-avatar{width:16px;height:16px;border-radius:50%;background:var(--heading)}

/* footer */
.site-footer{position:absolute;left:0;top:1122px;width:953px;height:78px;background:var(--footer);color:#bcbcbc;font-size:10.5px}
.footer-nav{position:absolute;left:0;top:17px;width:100%;text-align:center}
.footer-nav a{color:#cfcfcf;text-decoration:none;margin:0 4px}
.footer-rule{position:absolute;left:118px;top:41px;width:717px;height:1px;background:#2a2a2a;border-bottom:1px solid #4a4a4a}
.copyright{position:absolute;left:0;top:54px;width:100%;text-align:center;color:#a8a8a8}
</style>
</head>
<body>

<header class="site-header">
  <div class="brand"><span class="brand-mark"></span><span class="brand-name">Quanta Signs</span></div>
  <div class="store-locations">
    <svg width="16" height="18" viewBox="0 0 16 18"><rect x="7" y="0" width="2" height="18" fill="#1c1c1c"/><path d="M1 3h10l3 2-3 2H1z" fill="#1c1c1c"/><path d="M15 9H5L2 11l3 2h10z" fill="#1c1c1c"/></svg>
    Store Locations:<br>Harbourview (08) 5550 1184<br>Northgate (08) 5550 2231<br>Lakeside
  </div>
  <nav class="main-nav">
    <a class="active">Home</a><a>About Us</a><a>Services</a><a>Portfolio</a><a>Contact</a>
  </nav>
</header>

<section class="hero">
  <h1 class="hero-title">Sign Solution</h1>
  <p class="hero-text">Lorem ipsum dolor sit amet, consectetuer adipiscing elit. Aenean commodo ligula eget dolor. Aenean massa. Cum sociis natoque penatibus et magnis dis parturient montes, nascetur ridiculus mus. Donec quam felis, ultricies nec, pellentesque eu, pretium quis, sem.</p>
  <div class="slider-dots"><span class="on"></span><span></span><span></span><span></span></div>
  <div class="hero-visual" role="img" aria-label="Black A-frame sandwich board sign with an arrow, standing on the pavement"></div>
</section>

<h2 class="section-title" style="left:125px;top:463px">Welcome to our site</h2>
<div class="section-rule" style="left:290px;top:473px;width:553px"></div>
<p class="welcome-text">Quanta Signs is a West Australian owned and managed business offering shop signage, A frames, vinyl lettering, pull up banners, vehicle signage, in fact a complete service for your company when it comes to advertising their business. So if you're seeking quality signs, talk to our team. In hac habitasse platea dictumst. Curabitur at lacus ac velit ornare lobortis. Curabitur a felis in nunc fringilla tristique. Morbi mattis ullamcorper velit. Phasellus gravida semper nisi. Nullam vel sem. Pellentesque libero tortor, tincidunt et, tincidunt eget, semper nec, quam. Sed hendrerit. Morbi ac felis. Nunc egestas, augue at pellentesque laoreet, felis eros vehicula leo, at malesuada. velit leo quis pede. Donec interdum, metus et hendrerit dolor diam sagittis ligula, eget egestas libero turpis vel mi. Nunc nec neque.</p>
<div class="btn-more">more »</div>
<svg class="owner-badge" width="80" height="96" viewBox="0 0 80 96" role="img" aria-label="Ownership badge">
  <polygon points="40,4 74,24 74,64 40,84 6,64 6,24" fill="#1c1c1c"/>
</svg>

<form class="quote-panel">
  <div class="quote-badge"><strong>Need a Quote</strong><em>Request a quote online today</em></div>
  <span class="field-label" style="top:74px">Name *</span><span class="field" style="top:70px"></span>
  <span class="field-label" style="top:105px">Company*</span><span class="field" style="top:101px"></span>
  <span class="field-label" style="top:137px">Phone *</span><span class="field" style="top:133px"></span>
  <span class="field-label" style="top:168px">Email *</span><span class="field" style="top:164px"></span>
  <span class="field-label" style="top:199px">Suburb *</span><span class="field" style="top:195px"></span>
  <span class="field-label" style="top:230px">Store:</span><span class="field" style="top:226px"></span>
  <span class="field-label" style="top:262px">Sign type</span><span class="field" style="top:258px"></span>
  <span class="field-label" style="top:293px">Material</span><span class="field" style="top:289px"></span>
  <span class="field-label" style="top:324px">Sign Size</span><span class="field" style="top:320px"></span>
  <span class="field-label" style="top:355px">Need to Design?</span><span class="field" style="top:351px;left:104px;width:146px"></span>
  <span class="field-label" style="top:386px">Other</span><span class="field" style="top:383px;height:35px"></span>
  <div class="btn-send">Send</div>
</form>

<h2 class="section-title" style="left:125px;top:700px">Recent Work</h2>
<div class="section-rule" style="left:240px;top:710px;width:603px"></div>
<div class="work-arrow prev"><svg width="8" height="10" viewBox="0 0 8 10"><path d="M6 1L2 5l4 4" stroke="#fff" stroke-width="1.5" fill="none"/></svg></div>
<div class="work-thumb" style="left:178px" role="img" aria-label="Beauty and massage shop front with window signage"></div>
<div class="work-thumb highlight" style="left:337px" role="img" aria-label="Portfolio item on hover"></div>
<div class="work-thumb" style="left:496px" role="img" aria-label="Beauty and massage shop front with window signage"></div>
<div class="work-thumb" style="left:654px" role="img" aria-label="Beauty and massage shop front with window signage"></div>
<div class="work-arrow next"><svg width="8" height="10" viewBox="0 0 8 10"><path d="M2 1l4 4-4 4" stroke="#fff" stroke-width="1.5" fill="none"/></svg></div>

<h2 class="section-title" style="left:118px;top:910px">Why Choose Us?</h2>
<div class="section-rule" style="left:240px;top:920px;width:217px"></div>
<ul class="reasons">
  <li><svg width="12" height="12" viewBox="0 0 12 12"><circle cx="6" cy="6" r="6" fill="#2b4c85"/><path d="M5 3.5L7.5 6 5 8.5" stroke="#fff" stroke-width="1.4" fill="none"/></svg>Cras rutrum leo at odio volutpat id blandit fugiats ipsum ornare.</li>
  <li><svg width="12" height="12" viewBox="0 0 12 12"><circle cx="6" cy="6" r="6" fill="#2b4c85"/><path d="M5 3.5L7.5 6 5 8.5" stroke="#fff" stroke-width="1.4" fill="none"/></svg>Donec fermentum porttitor nunc, sit amet gravida est porttitor vel.</li>
  <li><svg width="12" height="12" viewBox="0 0 12 12"><circle cx="6" cy="6" r="6" fill="#2b4c85"/><path d="M5 3.5L7.5 6 5 8.5" stroke="#fff" stroke-width="1.4" fill="none"/></svg>Maecenas quis nisi in uctus adipiscing sed vehicula tellus amet dolore.</li>
  <li><svg width="12" height="12" viewBox="0 0 12 12"><circle cx="6" cy="6" r="6" fill="#2b4c85"/><path d="M5 3.5L7.5 6 5 8.5" stroke="#fff" stroke-width="1.4" fill="none"/></svg>Aenean faucibus sapien a odio varius aliquet voluptas sadips..</li>
  <li><svg width="12" height="12" viewBox="0 0 12 12"><circle cx="6" cy="6" r="6" fill="#2b4c85"/><path d="M5 3.5L7.5 6 5 8.5" stroke="#fff" stroke-width="1.4" fill="none"/></svg>Suspendisse venenatis euismod ve vestibulum volutpat nibh imperdiets.</li>
  <li><svg width="12" height="12" viewBox="0 0 12 12"><circle cx="6" cy="6" r="6" fill="#2b4c85"/><path d="M5 3.5L7.5 6 5 8.5" stroke="#fff" stroke-width="1.4" fill="none"/></svg>Quisque non leo molestie augue imperdiet sollicitudin eu nec urna.</li>
</ul>

<h2 class="section-title" style="left:473px;top:910px">What Client's Say</h2>
<div class="section-rule" style="left:602px;top:920px;width:211px"></div>
<blockquote class="testimonial">"Neque porro quisquam est, qui dolorem ipsum quia dolor sit amet, consec tetur, adipisci velit, sed quia non numquam eius modi tempora incidunt uts labore et dolore magnam aliquam quaerat voluptatem. Ut enim ad minimas veniam, quis nostrum exercitationem ullam corporis suscipit laboriosam, nisi ut aliquid ex ea commodi consequatur slores amet untras vel illum qui."</blockquote>
<div class="author"><span class="author-avatar"></span><span><b>Jon Doe,</b> Company Inc.</span></div>

<footer class="site-footer">
  <nav class="footer-nav"><a>Home</a>I<a>About Us</a>I<a>Services</a>I<a>Portfolio</a>I<a>Contact</a></nav>
  <div class="footer-rule"></div>
  <p class="copyright">2013 QuantaSigns, Inc. All rights reserved.</p>
</footer>

</body>
</html>
```